Raised Fingerprint Business Card Design

I need a business card design and I would like the image for the business cards to carry on to my stationary and website. My business is Forensic Consulting. I will be providing services to prosecuting and defense attorneys as well as law enforcement agencies in the areas of latent print comparison, crime scene investigations, and forensic training. I am looking for a color scheme of red, black, and silver. I would like a fingerprint that is raised and the text to be raised to some degree depending on your recommendations. with a fingerprint glass. I would like the card to include the business name, my name the deignation CLPE after it, phone number, web address, and physical address. I would like the phrase "veritas aequitas " placed discretely at the bottome of the card-subtle/not too bold.

Target Market(s)

Attorneys and law enforcement agencies

Industry/Entity Type

Business

Contact Information for Business Card

Delia Forsythe, CLPE
Brightwell Evidence Group, LLC
P.O. Box 583172 Sacramento, CA 95817
916.428.3071
www.brightwellevidencegroup.example
brightwellevidence@mailbox.example

Colors
ec1f27

Requirements
Must have
• Fingerprint and old fashioned handheld magnifying glass (Sherlock Holmes style.
• The Latin phrase listed above placed at the bottom of the front of the card discreetly.
Nice to have
• The fingerprint ridges (black lines) raised so the customer can feel it the texture.
• Raised lettering for either my name or the company name.
Should not have
• None that I can think of now.

```html
<!DOCTYPE html>
<html lang="en">
<head>
<meta charset="utf-8">
<title>Brightwell Evidence Group — Business Card</title>
<link rel="stylesheet" href="https://fonts.googleapis.com/css2?family=Roboto:wght@400;500;700&display=swap">
<style>
  :root {
    --stage: #e6e6e8;
    --ink: #1f1f21;
    --charcoal: #2a2a2c;
    --charcoal-deep: #1c1c1e;
    --paper: #f7f7f7;
    --muted: #8a8a8e;
    --red: #ec1f27;
    --white: #ffffff;
  }
  * { box-sizing: border-box; margin: 0; padding: 0; }
  html, body { width: 1200px; height: 1200px; overflow: hidden; }
  body {
    background: var(--stage);
    font-family: "Roboto", Arial, sans-serif;
    position: relative;
  }
  .card {
    position: absolute;
    left: 180px;
    width: 840px;
    height: 480px;
    overflow: hidden;
    box-shadow: 0 14px 30px rgba(0,0,0,.18);
  }

  /* Front */
  .card--front { top: 90px; background: var(--charcoal); }
  .front__skyline {
    position: absolute; left: 0; bottom: 0; width: 100%; height: 260px;
    background: linear-gradient(180deg, rgba(42,42,44,0) 0%, rgba(20,20,22,.55) 100%);
  }
  .front__print {
    position: absolute; left: 300px; top: 30px; width: 230px; height: 230px;
    border-radius: 50%;
    background: radial-gradient(circle, rgba(10,10,12,.55) 0%, rgba(10,10,12,.25) 55%, rgba(10,10,12,0) 72%);
  }
  .brand__name { font-weight: 700; letter-spacing: .2px; white-space: nowrap; }
  .card--front .brand__name {
    position: absolute; left: 0; right: 0; top: 228px; text-align: center;
    color: var(--white); font-size: 34px;
  }
  .front__motto {
    position: absolute; right: 70px; bottom: 36px;
    font-size: 9px; letter-spacing: 1.5px; text-transform: uppercase;
    color: var(--muted); opacity: .7;
  }

  /* Back */
  .card--back { top: 630px; background: var(--paper); }
  .back__band { position: absolute; inset: 0; }
  .back__visual {
    position: absolute; right: 50px; top: 80px; width: 270px; height: 230px;
    border-radius: 50%;
    background: radial-gradient(ellipse at 50% 50%, #9a9a9d 0%, #c9c9cc 45%, rgba(247,247,247,0) 72%);
  }
  .holder { position: absolute; left: 44px; top: 48px; }
  .holder__name { color: var(--red); font-weight: 700; font-size: 24px; }
  .holder__role { color: var(--ink); font-size: 16px; margin-top: 2px; }
  .card--back .brand__name {
    position: absolute; left: 44px; top: 130px;
    color: var(--ink); font-size: 26px;
  }
  .contact {
    position: absolute; left: 44px; top: 232px; list-style: none;
    display: flex; flex-direction: column; gap: 12px;
  }
  .contact__item { display: flex; align-items: center; gap: 10px; font-size: 17px; color: var(--ink); }
  .contact__icon { width: 18px; height: 18px; flex: none; }
  .back__web {
    position: absolute; left: 44px; bottom: 22px;
    color: var(--white); font-size: 16px; letter-spacing: .3px;
  }
</style>
</head>
<body>

  <section class="card card--front" aria-label="Card front">
    <div class="front__skyline" role="img" aria-label="Faint city skyline photograph"></div>
    <div class="front__print" role="img" aria-label="Faint dark fingerprint"></div>
    <p class="brand__name">Brightwell Evidence Group, LLC</p>
    <p class="front__motto">Veritas Aequitas</p>
  </section>

  <section class="card card--back" aria-label="Card back">
    <svg class="back__band" viewBox="0 0 840 480" preserveAspectRatio="none" aria-hidden="true">
      <polygon points="0,420 560,420 590,395 770,395 790,370 790,270 840,250 840,480 0,480" fill="var(--charcoal-deep)"/>
    </svg>
    <div class="back__visual" role="img" aria-label="Fingerprint under a handheld magnifying glass"></div>

    <div class="holder">
      <p class="holder__name">Delia Forsythe</p>
      <p class="holder__role">Owner</p>
    </div>

    <p class="brand__name">Brightwell Evidence Group, LLC</p>

    <ul class="contact">
      <li class="contact__item">
        <svg class="contact__icon" viewBox="0 0 18 18" aria-hidden="true">
          <circle cx="9" cy="9" r="8" fill="none" stroke="var(--red)" stroke-width="1.6"/>
          <path d="M6 5.5l1.6-.5 1 2-1 .8a5 5 0 0 0 2.6 2.6l.8-1 2 1-.5 1.6c-3.4.2-6.7-3.1-6.5-6.5z" fill="var(--red)"/>
        </svg>
        916.428.3071
      </li>
      <li class="contact__item">
        <svg class="contact__icon" viewBox="0 0 18 18" aria-hidden="true">
          <circle cx="9" cy="9" r="8" fill="none" stroke="var(--red)" stroke-width="1.6"/>
          <rect x="4.5" y="6" width="9" height="6.5" fill="none" stroke="var(--red)" stroke-width="1.3"/>
          <path d="M4.5 6l4.5 3.6L13.5 6" fill="none" stroke="var(--red)" stroke-width="1.3"/>
        </svg>
        brightwellevidence@mailbox.example
      </li>
      <li class="contact__item">
        <svg class="contact__icon" viewBox="0 0 18 18" aria-hidden="true">
          <circle cx="9" cy="9" r="8" fill="var(--red)"/>
          <path d="M9 4.5a3 3 0 0 0-3 3c0 2.3 3 5.8 3 5.8s3-3.5 3-5.8a3 3 0 0 0-3-3z" fill="var(--white)"/>
          <circle cx="9" cy="7.5" r="1.1" fill="var(--red)"/>
        </svg>
        P.O. Box 583172 Sacramento, CA 95817
      </li>
    </ul>

    <p class="back__web">www.brightwellevidencegroup.example</p>
  </section>

</body>
</html>
```